Jumbo direct mailing Postcard design

I need a design for an oversized postcard mailer that will be marketing a ballroom dance studio located in Larkfield, NC. We are an Celeste Varnholt franchised dance studio and considered the gold standard for ballroom dance lessons. Our instructors our certified and top quality. The size of the postcard is 8.5" x 5.5" and will be full color. Our website is carycelestevarnholt.example
This will be marketed to men and women. Average age is 30-60. Mostly females apply, but some males, see sliders.
We want an eye catching postcard to get people to call. We are offering a free dance lesson to people that either call or go to our website and fill out the form.
Some ideas we had for headlines are:
-
Bored in Larkfield? Looking for something new to try? Learn how to
-Spice up date night
-Meet new people at our dance parties
-Lose weight
-Gain confidence while learning a valuable social skill
-
We can discuss headlines and text in feedback discussion.
I will be uploading some creative assets you can use for this project, but are not required to be used at all. They are not the best looking creatives.
The final design should communicate a fun valuable social activity and skill to the reader and showing how our school is the best quality in the market. Using gold and black colors could accompany that.
Target Market(s)
men/women luxury market, age 30-60. affluent individuals
Industry/Entity Type
Dance Studio
Look and feel
Each slider illustrates characteristics of the customer's brand and the style your logo design should communicate.

```html
<!DOCTYPE html>
<html lang="en">
<head>
<meta charset="utf-8">
<title>Dance with me – Larkfield Celeste Varnholt Dance Studios</title>
<link rel="stylesheet" href="https://fonts.googleapis.com/css2?family=Great+Vibes&family=Parisienne&display=swap">
<style>
  :root {
    --ink: #000000;
    --gold: #f5e21c;
    --gold-soft: #fff27a;
    --gold-deep: #d9b400;
    --beam-dark: #0a0a0a;
    --beam-light: #6e6e6e;
    --script-display: "Great Vibes", cursive;
    --script-text: "Parisienne", cursive;
  }
  html, body {
    margin: 0;
    padding: 0;
    width: 1200px;
    height: 900px;
    overflow: hidden;
    background: var(--ink);
  }
  .postcard {
    position: relative;
    width: 1200px;
    height: 900px;
    overflow: hidden;
    background: var(--ink);
    color: var(--gold);
  }
  .light-beam {
    position: absolute;
    inset: 0;
  }
  .star {
    position: absolute;
    width: 18px;
    height: 18px;
  }
  .dancers {
    position: absolute;
    left: 68px;
    top: 165px;
    width: 425px;
    height: 560px;
    border-radius: 45% 40% 50% 50% / 30% 30% 45% 45%;
    background: radial-gradient(ellipse at 50% 45%, var(--gold-soft) 0%, var(--gold) 55%, var(--gold-deep) 100%);
  }
  .headline {
    position: absolute;
    left: 405px;
    top: 48px;
    margin: 0;
    font-family: var(--script-display);
    font-weight: 400;
    font-size: 136px;
    line-height: 1;
    color: var(--gold);
    white-space: nowrap;
  }
  .lead {
    position: absolute;
    left: 510px;
    top: 322px;
    margin: 0;
    font-family: var(--script-text);
    font-size: 42px;
    line-height: 1.2;
    color: var(--gold);
    white-space: nowrap;
  }
  .benefits {
    position: absolute;
    left: 630px;
    top: 392px;
    margin: 0;
    padding: 0;
    list-style: none;
    font-family: var(--script-text);
    font-size: 35px;
    line-height: 40px;
    color: var(--gold);
    white-space: nowrap;
  }
  .benefits li { margin-bottom: 16px; }
  .benefits li:last-child { margin-bottom: 0; }
  .studio {
    position: absolute;
    left: 562px;
    top: 672px;
    color: var(--gold);
  }
  .studio-city {
    display: block;
    margin-left: 8px;
    font-family: var(--script-display);
    font-size: 80px;
    line-height: 1;
  }
  .studio-name {
    display: block;
    margin-top: -14px;
    font-family: var(--script-text);
    font-size: 52px;
    line-height: 1.1;
    white-space: nowrap;
  }
  .studio-tag {
    display: block;
    margin-left: 100px;
    font-family: var(--script-text);
    font-size: 22px;
    line-height: 1;
    white-space: nowrap;
  }
</style>
</head>
<body>
<main class="postcard">
  <svg class="light-beam" width="1200" height="900" viewBox="0 0 1200 900" aria-hidden="true">
    <defs>
      <linearGradient id="beamFill" x1="0" y1="0" x2="1" y2="0.3">
        <stop offset="0" stop-color="#0a0a0a"/>
        <stop offset="0.35" stop-color="#1c1c1c"/>
        <stop offset="1" stop-color="#6e6e6e"/>
      </linearGradient>
    </defs>
    <path d="M400 470 Q 780 250 1200 105 L1200 900 L470 900 Q 440 690 400 470 Z" fill="url(#beamFill)"/>
  </svg>

  <svg class="star" style="left:82px;top:68px" viewBox="0 0 20 20" aria-hidden="true"><path d="M10 0 L12 8 L20 10 L12 12 L10 20 L8 12 L0 10 L8 8 Z" fill="var(--gold)"/></svg>
  <svg class="star" style="left:232px;top:88px" viewBox="0 0 20 20" aria-hidden="true"><path d="M10 0 L12 8 L20 10 L12 12 L10 20 L8 12 L0 10 L8 8 Z" fill="var(--gold)"/></svg>
  <svg class="star" style="left:122px;top:288px" viewBox="0 0 20 20" aria-hidden="true"><path d="M10 0 L12 8 L20 10 L12 12 L10 20 L8 12 L0 10 L8 8 Z" fill="var(--gold)"/></svg>

  <div class="dancers" role="img" aria-label="Gold silhouette of a ballroom dance couple in a waltz hold, standing on a curved gold swirl"></div>

  <h1 class="headline">Dance with me...</h1>

  <p class="lead">Looking for somthing new? Learn how to:</p>
  <ul class="benefits">
    <li>Spice up your date night</li>
    <li>Meet new people at our dance parties</li>
    <li>Lose weight</li>
    <li>Gain confidence while learning<br>a valuable social skill</li>
  </ul>

  <div class="studio">
    <span class="studio-city">Larkfield</span>
    <span class="studio-name">Celeste Varnholt</span>
    <span class="studio-tag">Franchised Dance Studios</span>
  </div>
</main>
</body>
</html>
```